WP website design (Brannick)

We need a wordpress design that will incorporate a professional color scheme with company logo in a clean layout. The design needs to consider that this will be developed on a responsive theme. Colors are undetermined - can use a dark red - logo is black so creative use of colors will be important. Client wants a 'modern' look.

Industry/Entity Type

It Company

Font styles to use
Serif
Sans Serif

Colors

Designer to choose colors to be used in the design.

Requirements
Must have
• Navigation: 1) Home 2) Auctions 3) Auction Services 4) Our Company 5) Contact Us

Site will have a slideshow element and the following widgets: 1) Featured Auctions 2) Testimonials blog widget 3) 'Auction Alerts' email sign up 4) Featured Videos

In the footer, there will be smaller company logo, the affiliations logo, and contact info below:
Brannick Auction & Realty” • 3816 Wickerby Lane •
Carrow, AR 72958 • (501) 555-0172 • tbrannick@mailvesta.example.
Nice to have
• - Site will have drop-down menus - please indicate the styling, for instance the dropdown menus 1) Upcoming Auctions 2) Past Auctions under the 'Auctions' link

```html
<!DOCTYPE html>
<html lang="en">
<head>
<meta charset="utf-8">
<title>Brannick Auction &amp; Realty</title>
<link href="https://fonts.googleapis.com/css2?family=Source+Sans+3:ital,wght@0,400;0,600;0,700;1,600&family=Kaushan+Script&display=swap" rel="stylesheet">
<style>
:root{
  --red:#a3131a;
  --red-dark:#7c0a0f;
  --black:#000;
  --ink:#1b1b1b;
  --panel:#eeeeee;
  --panel-line:#b9b9b9;
  --white:#fff;
  --sans:"Source Sans 3", sans-serif;
  --body:Arial, Helvetica, sans-serif;
}
*{box-sizing:border-box;margin:0;padding:0}
html,body{width:847px;height:1200px;overflow:hidden}
body{position:relative;background:linear-gradient(#f1f1f1 0,#fff 110px,#fff);font-family:var(--body);color:var(--ink)}
.abs{position:absolute}

/* brand */
.brand{left:72px;top:26px;font-family:var(--sans);font-weight:700;color:var(--black);line-height:1}
.brand-name{font-size:42px;letter-spacing:-.5px}
.brand-sub{font-size:14px;margin-left:92px;margin-top:2px}

/* nav */
.nav{left:70px;top:110px;width:706px;height:36px;background:linear-gradient(#b8171f,#8d0b11);border-radius:6px 6px 0 0;display:flex}
.nav a{display:block;height:36px;line-height:36px;color:var(--white);font-family:var(--sans);font-weight:600;font-size:12px;text-decoration:none;text-align:center;border-right:1px solid #6b080c}
.nav a.active{background:linear-gradient(#3a0204,#1a0000)}
.dropdown{left:158px;top:146px;width:138px;border:1px solid #c01a22;z-index:3}
.dropdown a{display:block;height:26px;line-height:26px;padding-left:6px;color:var(--white);font-family:var(--sans);font-size:11.5px;text-decoration:none}
.dropdown .up{background:var(--red)}
.dropdown .past{background:#000;border-top:1px solid #c01a22}

/* hero */
.hero-photo{left:70px;top:146px;width:502px;height:236px;background:linear-gradient(180deg,#4e6a37 0%,#7a4334 35%,#a8453a 60%,#5f7a3c 100%)}
.alerts{left:573px;top:146px;width:203px;height:240px;background:var(--black);color:var(--white);padding:22px 0 0 18px}
.alerts h2{font-family:var(--sans);font-weight:400;font-size:21px;margin-bottom:12px}
.alerts p{font-family:var(--sans);font-size:10.5px;line-height:14px;margin-bottom:10px;width:180px}
.alerts .email{width:174px;height:24px;background:var(--white);color:#888;font-size:9.5px;line-height:24px;padding-left:8px;margin-bottom:20px}
.alerts .btn{display:inline-block;background:var(--red);color:var(--white);font-family:var(--sans);font-weight:600;font-size:11.5px;padding:3px 13px}
.swoosh{left:0;top:330px}

/* intro */
.welcome{left:146px;top:396px;width:370px;text-align:center;font-family:"Kaushan Script",cursive;font-weight:400;font-size:18px;line-height:24px;color:var(--black);white-space:nowrap}
.tagline{left:74px;top:428px;font-family:var(--sans);font-size:13.5px;line-height:18px;color:var(--red)}
.intro{left:74px;top:453px;width:440px;font-size:10px;line-height:14.5px}

/* auction cards */
.card{left:77px;width:433px;height:220px;background:var(--panel);border:1px solid var(--panel-line);border-top:0}
.card-head{height:32px;line-height:33px;background:linear-gradient(#b8171f,#8d0b11);border-radius:6px 6px 0 0;color:var(--white);font-family:var(--sans);font-weight:700;font-size:12px;padding-left:15px;margin:0 -1px}
.card-thumb{left:25px;top:42px;width:113px;height:75px;background:linear-gradient(#b9c6c8 0%,#c9d0cd 30%,#7f8f5a 45%,#5e7235 100%);box-shadow:2px 2px 3px rgba(0,0,0,.35)}
.card-btn{left:51px;width:73px;height:24px;background:#000;border-radius:3px;color:var(--white);font-size:9.5px;line-height:24px;padding-left:27px}
.card-btn svg{position:absolute;left:8px;top:5px}
.card-info{left:157px;top:50px;width:270px;font-size:9.5px;line-height:13.5px}
.card-date{font-family:var(--sans);font-weight:700;font-size:12.5px;letter-spacing:.3px;margin-bottom:4px}
.salebill{display:block;margin:7px 0 8px 76px;color:var(--red-dark);font-family:var(--sans);font-weight:700;font-size:11px}
.loc{padding-left:12px;position:relative}
.loc svg{position:absolute;left:0;top:2px}
.loc-time{padding-left:47px}

/* sidebar widgets */
.widget{left:557px;width:218px;background:var(--panel);border:1px solid var(--panel-line);border-top:0}
.widget-head{height:32px;line-height:34px;background:var(--black);border-radius:6px 6px 0 0;color:var(--white);font-family:var(--sans);font-weight:600;font-size:18px;padding-left:13px;margin:0 -1px}
.feat-title,.feat-desc{text-align:center;font-size:8.5px;line-height:12.5px;margin-top:15px;padding:0 14px}
.feat-title{font-weight:700;color:#333}
.feat-photo{width:127px;height:77px;margin:8px auto 0;border:2px solid var(--red-dark);background:linear-gradient(#9fb2c6 0%,#c8c7c0 40%,#6c7f48 75%,#4c5b3a 100%)}
.video{margin:3px;height:152px;background:linear-gradient(90deg,#c9c9c4 0%,#a9a6a0 45%,#7b6c60 70%,#a45850 100%);position:relative}
.video-bar{position:absolute;left:0;right:0;bottom:0;height:13px;background:#d7d7d7;border-top:1px solid #999}
.quote{padding:16px 10px 0 16px;font-family:var(--sans);font-size:12px;line-height:15.5px;color:#333}
.quote .mark{color:var(--red);font-family:Georgia,serif;font-weight:700;font-size:22px;line-height:0;vertical-align:-5px}
.quote-by{padding:18px 0 0 16px;font-family:var(--sans);font-style:italic;font-weight:600;font-size:11px;color:#111}

/* footer */
.footer{left:0;top:1106px;width:847px;height:94px;background:#000;color:var(--white)}
.footer-info{left:77px;top:16px;font-size:10.5px;line-height:17px}
.footer-brand{left:420px;top:20px;font-family:var(--sans);font-weight:700;line-height:1}
.footer-brand .n{font-size:32px}
.footer-brand .s{font-size:10px;margin-left:72px}
.badge{top:28px;height:34px;background:#e6e6e6;border-radius:3px}
</style>
</head>
<body>

<div class="abs brand">
  <div class="brand-name">Brannick</div>
  <div class="brand-sub">Auction &amp; Realty</div>
</div>

<nav class="abs nav">
  <a href="#" style="width:88px">HOME</a>
  <a href="#" class="active" style="width:102px">AUCTIONS</a>
  <a href="#" style="width:150px">AUCTION SERVICES</a>
  <a href="#" style="width:126px">OUR COMPANY</a>
  <a href="#" style="width:112px;text-align:left;padding-left:24px;border-right:0">CONTACT US</a>
</nav>

<div class="abs dropdown">
  <a href="#" class="up">Upcoming auctions</a>
  <a href="#" class="past">Past auctions</a>
</div>

<div class="abs hero-photo" role="img" aria-label="Slideshow photo of a red brick family home with lawn and trees"></div>
<svg class="abs" style="left:538px;top:163px" width="19" height="19" viewBox="0 0 19 19"><circle cx="9.5" cy="9.5" r="9.5" fill="#000"/><path d="M5 13c1-4 4-5 7-5V5.5l4 4-4 4V11c-3 0-5 .5-7 2z" fill="#fff"/></svg>

<div class="abs alerts">
  <h2>Auction Alerts</h2>
  <p>Please join our free mailing list to get auction alerts for upcoming events.</p>
  <div class="email">Enter Your Email</div>
  <span class="btn">Subscribe</span>
</div>

<svg class="abs swoosh" width="847" height="70" viewBox="0 0 847 70">
  <path d="M61 62 Q 420 -22 799 62 Q 420 8 61 62 Z" fill="#7c0a0f"/>
</svg>

<h1 class="abs welcome">Welcome to Brannick Auction and Realty</h1>
<p class="abs tagline">Serving Western Arkansas and Eastern Oklahoma since 1982</p>
<p class="abs intro">In the auction business since 1982, Brannick Auction &amp; Realty was founded to provide the highest quality of auction service in the area. Dale Brannick and his son, Wes, conduct more than 100 auctions each year in Arkansas and Oklahoma.</p>

<section class="abs card" style="top:530px">
  <div class="card-head">ART, FURNITURE AND ACCESSORIES ONLINE AUCTION</div>
  <div class="abs card-thumb" role="img" aria-label="Photo of open grassland tract"></div>
  <div class="abs card-btn" style="top:133px"><svg width="14" height="14"><rect x="1" y="2" width="12" height="10" rx="2" fill="#fff"/><path d="M4 6h6M4 9h4" stroke="#000"/></svg>Details</div>
  <div class="abs card-btn" style="top:165px"><svg width="14" height="14"><rect x="1" y="2" width="12" height="10" fill="#fff"/><path d="M2 11l4-4 3 3 2-2 2 3z" fill="#3a8a2c"/></svg>Photos</div>
  <div class="abs card-info">
    <div class="card-date">THURSDAY, AUGUST 21ST AT 10:00 A.M.</div>
    <div>Selling 3120 Acres of land in tracts of 2590 Acres<br>&amp; 560 Acres</div>
    <span class="salebill">Click here to view Sale Bill!</span>
    <div><b>LIVE OFF-SITE AUCTION</b></div>
    <div><b>Auction Location:</b></div>
    <div class="loc"><svg width="8" height="10"><path d="M4 10 1 5a3 3 0 1 1 6 0z" fill="#c0141b"/></svg>118 N Cedar Ave, Dalton, OK 73851</div>
    <div><b>Property Location:</b></div>
    <div class="loc"><svg width="8" height="10"><path d="M4 10 1 5a3 3 0 1 1 6 0z" fill="#c0141b"/></svg>118 N Cedar Ave, Dalton, OK 73851</div>
    <div class="loc-time">08/21/14 at 10:00 AM CDT</div>
  </div>
</section>

<section class="abs card" style="top:778px">
  <div class="card-head">ART, FURNITURE AND ACCESSORIES ONLINE AUCTION</div>
  <div class="abs card-thumb" role="img" aria-label="Photo of open grassland tract"></div>
  <div class="abs card-btn" style="top:133px"><svg width="14" height="14"><rect x="1" y="2" width="12" height="10" rx="2" fill="#fff"/><path d="M4 6h6M4 9h4" stroke="#000"/></svg>Details</div>
  <div class="abs card-btn" style="top:165px"><svg width="14" height="14"><rect x="1" y="2" width="12" height="10" fill="#fff"/><path d="M2 11l4-4 3 3 2-2 2 3z" fill="#3a8a2c"/></svg>Photos</div>
  <div class="abs card-info">
    <div class="card-date">THURSDAY, AUGUST 21ST AT 10:00 A.M.</div>
    <div>Selling 3120 Acres of land in tracts of 2590 Acres<br>&amp; 560 Acres</div>
    <span class="salebill">Click here to view Sale Bill!</span>
    <div><b>LIVE OFF-SITE AUCTION</b></div>
    <div><b>Auction Location:</b></div>
    <div class="loc"><svg width="8" height="10"><path d="M4 10 1 5a3 3 0 1 1 6 0z" fill="#c0141b"/></svg>118 N Cedar Ave, Dalton, OK 73851</div>
    <div><b>Property Location:</b></div>
    <div class="loc"><svg width="8" height="10"><path d="M4 10 1 5a3 3 0 1 1 6 0z" fill="#c0141b"/></svg>118 N Cedar Ave, Dalton, OK 73851</div>
    <div class="loc-time">08/21/14 at 10:00 AM CDT</div>
  </div>
</section>

<aside class="abs widget" style="top:414px;height:230px">
  <div class="widget-head">Featured Auctions</div>
  <div class="feat-title">13.35 ACRES OF PRIME DEVELOP<br>&amp; 33RD STREET</div>
  <div class="feat-photo" role="img" aria-label="Photo of a house with a crowd gathered outside for an auction"></div>
  <div class="feat-desc" style="margin-top:16px">LOTS 13 &amp; 14 FOR SALE, MARLOW IOWA<br>Fourth Street, Marlow, IA 52640</div>
</aside>

<aside class="abs widget" style="top:678px;height:189px">
  <div class="widget-head">Featured Videos</div>
  <div class="video" role="img" aria-label="Video still of auctioneers addressing a crowd outdoors">
    <svg class="abs" style="left:83px;top:42px" width="48" height="48"><circle cx="24" cy="24" r="24" fill="#222" opacity=".85"/><path d="M18 13l18 11-18 11z" fill="#fff"/></svg>
    <div class="video-bar"><svg width="212" height="12"><path d="M4 3l6 3-6 3z" fill="#222"/><rect x="16" y="5" width="90" height="2" fill="#c0141b"/><circle cx="19" cy="6" r="3" fill="#555"/><rect x="106" y="5" width="25" height="2" fill="#999"/><rect x="185" y="3" width="10" height="6" fill="#333"/><rect x="199" y="3" width="10" height="6" fill="#333"/></svg></div>
  </div>
</aside>

<aside class="abs widget" style="top:895px;height:189px">
  <div class="widget-head">Testimonials Blog</div>
  <p class="quote"><span class="mark">&ldquo;</span> Using R. Calloway &amp; Associates to take listings from "old" to "sold" is a win-win experience that I recommend to other brokers in need of assistance in marketing their Stale Listings. <span class="mark">&rdquo;</span></p>
  <p class="quote-by">..Nate Perrow</p>
</aside>

<footer class="abs footer">
  <div class="abs footer-info">
    Brannick Auction &amp; Realty&rdquo;<br>
    &bull; 3816 Wickerby Lane &bull;<br>
    Carrow, AR 72958 &bull; (501) 555-0172 &bull; tbrannick@mailvesta.example<br>
    Copyright &copy; 2014: Brannick Auction &amp; Realty Inc.
  </div>
  <div class="abs footer-brand">
    <div class="n">Brannick</div>
    <div class="s">Auction &amp; Realty</div>
  </div>
  <div class="abs badge" style="left:600px;width:36px"></div>
  <div class="abs badge" style="left:648px;width:28px"></div>
  <div class="abs badge" style="left:686px;width:26px"></div>
  <div class="abs badge" style="left:724px;width:32px"></div>
</footer>

</body>
</html>
```